Brixel Information Technology Solutions
We are an Information Technology Company. We provide computer services to commercial companies. We would like a new card full color front and back with bleeding edge.
We have a logo that you can use or if you want to come up with a new logo that is fine too.
Our colors are mostly Maroon and black but be creative.
Sample Information
Grant P Oswick
4818 W Saguaro Ridge Drive
Suite 410
Phoenix, AZ 85016
O: 602.555.0143
C: 602.555.0178
24/7: 888.555.0162
goswick@brixelit.com
www.brixelit.com
Target Market(s)
Business of all sizes
Industry/Entity Type
Computer
Requirements
Must have
- Bleeding edge
full color on both sides

```html
<!DOCTYPE html>
<html lang="en">
<head>
<meta charset="utf-8">
<title>Brixel Information Technology Solutions — Business Card</title>
<link rel="stylesheet" href="https://fonts.googleapis.com/css2?family=Arimo:wght@400;700&display=swap">
<style>
  :root {
    --backdrop: #3b3b3c;
    --card-light: #ececec;
    --band-grey: #6a6a6b;
    --brand-grey: #5d5d5f;
    --brand-red: #c8262c;
    --text-light: #f4f4f4;
  }
  * { margin: 0; padding: 0; box-sizing: border-box; }
  html, body { width: 1200px; height: 534px; overflow: hidden; }
  body {
    background: var(--backdrop);
    font-family: "Arimo", Arial, sans-serif;
    position: relative;
  }
  .card {
    position: absolute;
    top: 119px;
    width: 517px;
    height: 294px;
    background: var(--card-light);
    overflow: hidden;
  }
  .card--front { left: 62px; }
  .card--back { left: 622px; }

  .brand { position: absolute; display: flex; align-items: center; }
  .brand__dot { border-radius: 50%; background: var(--brand-red); flex: none; }
  .brand__words { color: var(--brand-grey); font-weight: 700; }
  .brand__name { display: block; line-height: 1; }
  .brand__tagline { display: block; border-top: 1px solid var(--brand-grey); }

  .card--front .brand { left: 46px; top: 70px; }
  .card--front .brand__dot { width: 118px; height: 118px; margin-right: 22px; }
  .card--front .brand__name { font-size: 54px; letter-spacing: 9px; }
  .card--front .brand__tagline { font-size: 10.5px; letter-spacing: 0.9px; margin-top: 6px; padding-top: 3px; }

  .front__band {
    position: absolute; left: 0; bottom: 0; width: 100%; height: 35px;
    background: var(--band-grey);
    color: var(--text-light);
    font-size: 15px; letter-spacing: 6px;
    display: flex; align-items: center; justify-content: center;
  }

  .card--back .brand { left: 24px; top: 19px; }
  .card--back .brand__dot { width: 80px; height: 80px; margin-right: 14px; }
  .card--back .brand__name { font-size: 36px; letter-spacing: 6px; }
  .card--back .brand__tagline { font-size: 7.2px; letter-spacing: 0.6px; margin-top: 4px; padding-top: 2px; }

  .back__panel {
    position: absolute; left: 0; top: 117px; width: 100%; height: 177px;
    background: var(--band-grey);
    color: var(--text-light);
    font-size: 11.5px; line-height: 16px;
  }
  .back__pointer { position: absolute; left: 48px; top: 117px; }
  .person { position: absolute; left: 48px; top: 32px; }
  .person__name { color: var(--brand-red); font-size: 13.5px; }
  .person__address { margin-top: 12px; }
  .contact {
    position: absolute; left: 295px; top: 33px;
    padding-left: 10px;
  }
  .contact__phones { border-left: 1px solid var(--brand-red); margin-left: -10px; padding-left: 10px; }
  .contact__label, .contact__web { color: var(--brand-red); }
  .contact__online { margin-top: 16px; }
</style>
</head>
<body>
  <section class="card card--front">
    <div class="brand">
      <span class="brand__dot"></span>
      <span class="brand__words">
        <span class="brand__name">BRIXEL</span>
        <span class="brand__tagline">INFORMATION TECHNOLOGY SOLUTIONS</span>
      </span>
    </div>
    <div class="front__band">WWW.BRIXELIT.COM</div>
  </section>

  <section class="card card--back">
    <div class="brand">
      <span class="brand__dot"></span>
      <span class="brand__words">
        <span class="brand__name">BRIXEL</span>
        <span class="brand__tagline">INFORMATION TECHNOLOGY SOLUTIONS</span>
      </span>
    </div>
    <div class="back__panel">
      <div class="person">
        <p class="person__name">Grant P Oswick</p>
        <p class="person__role">Position</p>
        <p class="person__address">4818 W Saguaro Ridge Drive<br>Suite 410<br>Phoenix, AZ 85016</p>
      </div>
      <div class="contact">
        <div class="contact__phones">
          <p><span class="contact__label">O:</span> 602.555.0143</p>
          <p><span class="contact__label">C:</span> 602.555.0178</p>
          <p><span class="contact__label">24/7:</span> 888.555.0162</p>
        </div>
        <div class="contact__online">
          <p><span class="contact__label">Email:</span> goswick@brixelit.com</p>
          <p class="contact__web">www.brixelit.com</p>
        </div>
      </div>
    </div>
    <svg class="back__pointer" width="26" height="13" viewBox="0 0 26 13" aria-hidden="true">
      <polygon points="0,0 26,0 13,13" fill="var(--card-light)"/>
    </svg>
  </section>
</body>
</html>
```